Pharmaceutical Manufacturing Services Advertisement

We need a new full page advertisement designed for publication in international magazines. We are a custom pharmaceutical manufacturing company and we help biotechnology companies scale up their drug development for clinical trials. The products we help manufacture are therapeutics for global healthcare problems.

Target Market(s)

Verott Bio is a privately owned contract development manufacturing organisation (CDMO) headquartered in Darra, QLD, Australia.

Our mission is to is to be a global leader in development and in the provision of contract manufacturing for active pharmaceutical ingredient processes.

Why we do what we Do:

To help advance Biotechnology Companies so that they can deliver innovative therapeutics
~ enabling patients to live longer, healthier and happier lives
~ which solves worldwide health problems

Verott Bio’s role is to develop, implement and scale up the production to deliver biologic medicines for patients in partnership with the biotechnology companies.

Industry/Entity Type

Biotechnology

Font styles to use
Sans Serif

Colors

Designer to choose colors to be used in the design.

Requirements
Must have
• Please see the script on the Word document. There are 4 optional Header Taglines. Additional ideas for multiple designs for the taglines welcomed.
• However preference is for either of the first two:
• 1. Building your vision for better healthcare
• 2. Bridging your vision for better healthcare
• File Specs:
• • All artwork should be submitted as high-resolution (300 min. dpi), press-ready PDF files
• • CMYK color only
• • Full page 8.25” x 10.812”; 209.55 x 274.62 mm
• • Live Area for all sizes: 0.25” (6.35 mm) inside the trim
• • Bleed Area for all sizes: Extends 0.125” (3.175 mm) from trim
Nice to have
• Modern Science look to inspire biotechnology companies to work with us.
• Search for images to use by keyword "recombinant dna"

```html
<!DOCTYPE html>
<html lang="en">
<head>
<meta charset="utf-8">
<title>Verott Bio – Full Page Advertisement</title>
<link rel="stylesheet" href="https://fonts.googleapis.com/css2?family=Comfortaa:wght@300&family=Lato:wght@700;900&family=Raleway:wght@800&family=Rubik:wght@400;500;700&display=swap">
<style>
  :root {
    --navy: #1c3b5c;
    --lime: #b8c744;
    --sky: #42a4cc;
    --sky-soft: rgba(96, 170, 210, 0.55);
    --page-bg: #e8e9eb;
    --paper: #ffffff;
  }
  * { margin: 0; padding: 0; box-sizing: border-box; }
  html, body { width: 1200px; height: 1200px; overflow: hidden; }
  body { background: var(--page-bg); position: relative; font-family: "Rubik", sans-serif; color: var(--navy); }

  .advert {
    position: absolute; left: 158px; top: 26px;
    width: 883px; height: 1148px;
    background: var(--paper); overflow: hidden;
    box-shadow: 0 6px 24px rgba(0,0,0,0.18);
  }
  .advert-shapes { position: absolute; inset: 0; }

  .brand-name {
    position: absolute; right: 48px; top: 478px;
    font-family: "Lato", sans-serif; font-weight: 900;
    font-size: 56px; letter-spacing: 1px; color: var(--navy); line-height: 1;
  }
  .headline {
    position: absolute; right: 48px; top: 575px; text-align: right;
    font-family: "Raleway", sans-serif; font-weight: 800;
    font-size: 33px; line-height: 44px; color: var(--navy); letter-spacing: -0.3px;
  }
  .headline-rule {
    position: absolute; left: 385px; right: 0; top: 678px;
    height: 4px; background: var(--lime);
  }
  .subheadline {
    position: absolute; right: 48px; top: 686px; text-align: right;
    font-family: "Comfortaa", sans-serif; font-weight: 300;
    font-size: 33px; line-height: 36px; color: var(--navy);
  }
  .intro {
    position: absolute; left: 45px; right: 48px; top: 772px;
    font-size: 14.6px; line-height: 19px; text-align: justify;
    text-align-last: justify; color: var(--navy);
  }
  .intro strong { font-weight: 700; }
  .offer { position: absolute; top: 886px; }
  .offer-products { left: 45px; }
  .offer-services { left: 254px; top: 884px; }
  .offer-title {
    font-family: "Rubik", sans-serif; font-weight: 500;
    font-size: 22px; color: var(--sky); line-height: 30px; margin-bottom: 2px;
  }
  .offer-list { list-style: none; }
  .offer-list li {
    font-size: 16px; font-weight: 500; line-height: 21px; padding-left: 14px; position: relative;
  }
  .offer-list li::before {
    content: ""; position: absolute; left: 1px; top: 8px;
    width: 6px; height: 6px; border-radius: 50%; background: var(--lime);
  }

  .contact-bar { position: absolute; left: 0; top: 1055px; height: 93px; width: 820px; }
  .visit {
    position: absolute; left: 45px; top: 33px;
    font-family: "Lato", sans-serif; font-weight: 700; font-size: 26px; color: var(--navy);
    display: flex; align-items: center; gap: 6px;
  }
  .divider { position: absolute; left: 346px; top: 17px; width: 3px; height: 42px; background: var(--paper); }
  .contact-lines {
    position: absolute; left: 374px; top: 18px;
    font-family: "Lato", sans-serif; font-weight: 700; font-size: 16px; line-height: 21px; color: var(--navy);
  }
  .contact-lines div { display: flex; align-items: center; gap: 7px; }
</style>
</head>
<body>
  <main class="advert">
    <svg class="advert-shapes" width="883" height="1148" viewBox="0 0 883 1148" aria-hidden="false">
      <defs>
        <linearGradient id="labGradient" x1="0" y1="0" x2="1" y2="1">
          <stop offset="0" stop-color="#d9ebf5"/>
          <stop offset="0.45" stop-color="#a9cfe4"/>
          <stop offset="0.7" stop-color="#c8d8e4"/>
          <stop offset="1" stop-color="#8fbcd6"/>
        </linearGradient>
        <radialGradient id="labGlow" cx="0.48" cy="0.55" r="0.35">
          <stop offset="0" stop-color="#f4d9de" stop-opacity="0.9"/>
          <stop offset="0.6" stop-color="#d9b9b0" stop-opacity="0.35"/>
          <stop offset="1" stop-color="#d9b9b0" stop-opacity="0"/>
        </radialGradient>
      </defs>
      <rect class="top-band" x="0" y="0" width="883" height="45" fill="var(--lime)"/>
      <g role="img" aria-label="Photograph of a scientist in a laboratory holding forceps, overlaid with DNA helices and a molecular network">
        <polygon points="0,45 883,45 883,110 716,275 271,710 0,455" fill="url(#labGradient)"/>
        <polygon points="0,45 883,45 883,110 716,275 271,710 0,455" fill="url(#labGlow)"/>
      </g>
      <polygon class="tint-triangle" points="0,175 271,710 0,455" fill="var(--sky-soft)"/>
      <polygon class="accent-triangle" points="883,110 716,275 883,415" fill="var(--lime)"/>
      <polygon class="accent-stripe" points="733,296 741,290 883,405 883,419" fill="var(--sky)"/>
      <polygon class="footer-triangle" points="883,850 698,1030 828,1148 883,1148" fill="var(--sky)"/>
      <polygon class="footer-band" points="0,1055 725,1055 828,1148 0,1148" fill="var(--lime)"/>
    </svg>

    <div class="brand-name">VEROTT BIO</div>

    <h1 class="headline">BRIDGING YOUR VISION<br>FOR BETTER HEALTHCARE</h1>
    <div class="headline-rule"></div>
    <h2 class="subheadline">Your Partner in Early Phase<br>Clinical Biomanufacturing</h2>

    <p class="intro">We have been serving the pharmaceutical, biotechnology and veterinary industry for over <strong>20 years</strong> so you can create innovative medicines for worldwide health problems. Get your therapeutics to the patient faster with cost-effective manufacturing for your GMP clinical trial material. We offer rapid technology transfer, scale-up development and manufacturing of microbial cell-derived proteins at up to 500L scale. We prepare your active pharmaceutical ingredient (API) products to a world class standard ready for clinical development.</p>

    <section class="offer offer-products">
      <h3 class="offer-title">PRODUCTS</h3>
      <ul class="offer-list">
        <li>Recombinant proteins</li>
        <li>Live Biotherapeutics</li>
        <li>Bacterial vaccines</li>
        <li>Plasmid DNA</li>
      </ul>
    </section>
    <section class="offer offer-services">
      <h3 class="offer-title">SERVICES</h3>
      <ul class="offer-list">
        <li>Bacterial / Yeast Fermentation</li>
        <li>Cell Banking</li>
        <li>Process Development/Scale-up</li>
        <li>cGMP Manufacture of biopharmaceutical APIs</li>
        <li>Stability Testing</li>
      </ul>
    </section>

    <footer class="contact-bar">
      <div class="visit">
        <span>Visit</span>
        <svg width="24" height="24" viewBox="0 0 24 24" fill="none" stroke="var(--navy)" stroke-width="2">
          <circle cx="12" cy="12" r="10"/><ellipse cx="12" cy="12" rx="4.5" ry="10"/><line x1="2" y1="12" x2="22" y2="12"/>
        </svg>
        <span>verottbio.com.au</span>
      </div>
      <div class="divider"></div>
      <div class="contact-lines">
        <div>
          <svg width="15" height="15" viewBox="0 0 24 24" fill="none" stroke="var(--paper)" stroke-width="2.4"><path d="M5 3h4l2 5-2.5 1.5a11 11 0 0 0 6 6L16 13l5 2v4a2 2 0 0 1-2 2A16 16 0 0 1 3 5a2 2 0 0 1 2-2z"/></svg>
          <span>Australia +61(7)30004812</span>
        </div>
        <div>
          <svg width="15" height="15" viewBox="0 0 24 24" fill="none" stroke="var(--paper)" stroke-width="2.4"><rect x="2" y="5" width="20" height="14" rx="1"/><polyline points="2,6 12,13 22,6"/></svg>
          <span>enquiries@verottbio.com.au</span>
        </div>
      </div>
    </footer>
  </main>
</body>
</html>
```